Breezeway Comfort business cards design

Need a business card design for a Heating and Air Conditioning business. I need these items included.
Business name: Breezeway Comfort
Owner: Marcus Tollefsen
License # 2874590
Phone number # 555-382-4071
Email: breezewaycomfortair@mailvista.example
Sales
Service
Installation
Maintenance

Heating and Air Conditioning

Requirements
Must have
• Company name , license number , phone number , email

```html
<!DOCTYPE html>
<html lang="en">
<head>
<meta charset="utf-8">
<title>Breezeway Comfort – Business Cards</title>
<link rel="stylesheet" href="https://fonts.googleapis.com/css2?family=Montserrat:wght@400;500;700&display=swap">
<style>
  :root {
    --bg: #2b2b2c;
    --card: #1b1b1c;
    --front-ink: #8d8e90;
    --front-dot: #3a3a3c;
    --blue: #2148b8;
    --orange: #f2743a;
    --pink: #e8356b;
    --white: #f1f1f1;
  }
  * { box-sizing: border-box; margin: 0; padding: 0; }
  html, body {
    width: 1200px; height: 689px; overflow: hidden;
    background: var(--bg);
    font-family: "Montserrat", sans-serif;
  }
  .canvas { position: relative; width: 1200px; height: 689px; }
  .card {
    position: absolute; top: 190px;
    width: 540px; height: 309px;
    background: var(--card);
    border-radius: 18px;
    box-shadow: 0 18px 40px rgba(0,0,0,.45);
  }
  .card--front { left: 40px; }
  .card--back { left: 620px; }

  /* Front */
  .front-brand {
    position: absolute; inset: 0;
    display: flex; flex-direction: column; align-items: center; justify-content: center; gap: 18px;
  }
  .front-brand__dot { width: 58px; height: 58px; border-radius: 50%; background: var(--front-dot); }
  .front-brand__name {
    color: var(--front-ink); font-weight: 700; font-size: 40px;
    letter-spacing: 2px; text-transform: uppercase; text-align: center; line-height: 1.1;
  }

  /* Back */
  .back-brand {
    position: absolute; left: 28px; top: 70px; width: 170px;
    display: flex; flex-direction: column; align-items: center; gap: 12px;
  }
  .back-brand__dot { width: 44px; height: 44px; border-radius: 50%; background: var(--orange); }
  .back-brand__name {
    color: var(--blue); font-weight: 700; font-size: 24px;
    text-transform: uppercase; letter-spacing: 1px; text-align: center; line-height: 1.1;
  }
  .divider {
    position: absolute; left: 206px; top: 52px; width: 2px; height: 170px;
    background: linear-gradient(var(--orange), var(--pink));
  }
  .contact { position: absolute; left: 226px; top: 50px; color: var(--white); }
  .contact__name { color: var(--blue); font-weight: 700; font-size: 26px; line-height: 1.1; }
  .contact__role { color: var(--orange); font-size: 15px; margin-bottom: 18px; }
  .contact__line { font-size: 14px; margin-bottom: 10px; display: flex; align-items: center; gap: 8px; }
  .contact__line--email { font-size: 12.5px; }
  .contact__icon { width: 14px; height: 14px; flex: none; }
  .services {
    position: absolute; left: 0; right: 0; bottom: 30px;
    display: flex; justify-content: center; gap: 16px;
    color: var(--white); font-size: 15px; font-weight: 500;
  }
  .services__item { display: flex; align-items: center; gap: 7px; }
  .services__dot { width: 8px; height: 8px; border-radius: 50%; background: var(--orange); }
</style>
</head>
<body>
<main class="canvas">
  <section class="card card--front">
    <div class="front-brand">
      <span class="front-brand__dot"></span>
      <p class="front-brand__name">Breezeway<br>Comfort</p>
    </div>
  </section>

  <section class="card card--back">
    <div class="back-brand">
      <span class="back-brand__dot"></span>
      <p class="back-brand__name">Breezeway<br>Comfort</p>
    </div>
    <span class="divider"></span>
    <div class="contact">
      <p class="contact__name">Marcus Tollefsen</p>
      <p class="contact__role">Owner</p>
      <p class="contact__line">License # 2874590</p>
      <p class="contact__line">
        <svg class="contact__icon" viewBox="0 0 24 24"><path fill="#f2743a" d="M6.6 10.8a15.1 15.1 0 0 0 6.6 6.6l2.2-2.2a1 1 0 0 1 1-.25 11.4 11.4 0 0 0 3.6.57 1 1 0 0 1 1 1V20a1 1 0 0 1-1 1A17 17 0 0 1 3 4a1 1 0 0 1 1-1h3.5a1 1 0 0 1 1 1c0 1.25.2 2.45.57 3.57a1 1 0 0 1-.25 1z"/></svg>
        # 555-382-4071
      </p>
      <p class="contact__line contact__line--email">
        <svg class="contact__icon" viewBox="0 0 24 24"><rect x="2" y="5" width="20" height="14" rx="2" fill="#e8356b"/><path d="M3 6l9 7 9-7" stroke="#1b1b1c" stroke-width="2" fill="none"/></svg>
        breezewaycomfortair@mailvista.example
      </p>
    </div>
    <ul class="services">
      <li class="services__item"><span class="services__dot"></span>Sales</li>
      <li class="services__item"><span class="services__dot"></span>Service</li>
      <li class="services__item"><span class="services__dot"></span>Installation</li>
      <li class="services__item"><span class="services__dot"></span>Maintenance</li>
    </ul>
  </section>
</main>
</body>
</html>
```